Business Cards and A-Frame Sign for Keystone Physio

Keystone Physio is a Physiotherapy clinic with multiple locations. We have recently had our logo and branding redesigned and require the following:

New A-Frame Sign Posters (36 inch x 24 inch)

A-frame design requirements
- business name and logo
- information about what we do (see www.harlowkeystonephysio-example.com for information)
- addresses
- contact details (phone and email)

Our practice details are:

1. Keystone Physio Ridgeview
284 Mabel Street, Ridgeview QLD 4005

2. Keystone Physio Millyard
Within Tallis Court
Lobby 1, Level 2, Millyard Square
58 Quillan Parade, Ashbrook QLD 4006

3. Keystone Physio Westmere
Within Brightwell Medical Centre
Suite 6a, Level 1
812 Pemberton Road, Westmere QLD 4011

Phone: 07 3190 5627
Email: info@harlowkeystonephysio-example.com

```html
<!DOCTYPE html>
<html lang="en">
<head>
<meta charset="utf-8">
<title>Keystone Physio – Business Cards</title>
<link href="https://fonts.googleapis.com/css2?family=Lato:wght@400;700&display=swap" rel="stylesheet">
<style>
  :root {
    --page-bg: #e9eaec;
    --card-bg: #ffffff;
    --brand-blue: #2f8fd5;
    --text-dark: #3f3f3f;
    --text-grey: #6b6b6b;
    --rule-grey: #9aa7b3;
  }
  * { box-sizing: border-box; margin: 0; padding: 0; }
  html, body { width: 1200px; height: 928px; overflow: hidden; }
  body {
    background: var(--page-bg);
    font-family: "Lato", Arial, sans-serif;
    position: relative;
  }
  .card {
    position: absolute;
    width: 600px;
    height: 343px;
    background: var(--card-bg);
    box-shadow: 0 6px 18px rgba(0,0,0,0.18);
    overflow: hidden;
  }
  .card--appointment { left: 70px; top: 70px; }
  .card--contact { left: 530px; top: 490px; }

  .brand {
    display: flex;
    align-items: center;
    gap: 8px;
    color: var(--brand-blue);
    font-weight: 700;
    letter-spacing: 0.06em;
    text-transform: uppercase;
    white-space: nowrap;
  }
  .brand__dot {
    width: 13px; height: 13px;
    border-radius: 50%;
    background: var(--brand-blue);
    flex: none;
  }
  .card--appointment .brand {
    position: absolute; left: 30px; top: 156px; font-size: 17px;
  }
  .card--contact .brand {
    position: absolute; right: 30px; top: 30px; font-size: 16px;
  }

  .appointment {
    position: absolute; left: 272px; top: 58px; width: 300px;
  }
  .appointment__title {
    color: var(--brand-blue);
    font-weight: 700;
    font-size: 15px;
    letter-spacing: 0.04em;
    margin-bottom: 18px;
    white-space: nowrap;
  }
  .days { display: flex; gap: 10px; margin-bottom: 26px; }
  .day {
    display: flex; align-items: center; gap: 4px;
    font-size: 11px; color: var(--text-dark);
  }
  .day__box {
    width: 10px; height: 10px; border: 1px solid var(--text-dark);
  }
  .field-row { display: flex; gap: 10px; margin-bottom: 22px; }
  .field {
    display: flex; align-items: flex-end; flex: 1;
    color: var(--brand-blue); font-size: 12px; font-weight: 700;
    letter-spacing: 0.05em; white-space: nowrap;
  }
  .field__line {
    flex: 1; border-bottom: 1px dotted var(--rule-grey);
    margin-left: 6px; height: 12px;
  }

  .contact { position: absolute; left: 36px; top: 72px; width: 520px; }
  .contact__name {
    color: var(--brand-blue); font-size: 20px; font-weight: 700; line-height: 1.1;
  }
  .contact__role { color: var(--text-dark); font-size: 15px; margin-bottom: 2px; }
  .contact__web { color: var(--text-grey); font-size: 10px; margin-bottom: 10px; }
  .contact__line {
    display: flex; align-items: center; gap: 8px;
    color: var(--text-grey); font-size: 11px; line-height: 1.4;
  }
  .icon { width: 11px; height: 11px; flex: none; fill: var(--brand-blue); }
  .location {
    display: flex; align-items: flex-start; gap: 8px;
    margin-top: 8px;
    color: var(--text-dark); font-size: 11px; line-height: 1.35;
  }
  .location .icon { margin-top: 10px; height: 13px; }
  .location__name { color: var(--text-grey); }
</style>
</head>
<body>

<section class="card card--appointment">
  <div class="brand"><span class="brand__dot"></span>Keystone Physio</div>
  <div class="appointment">
    <h2 class="appointment__title">YOUR NEXT APPOINTMENT</h2>
    <div class="days">
      <span class="day"><span class="day__box"></span>Mon</span>
      <span class="day"><span class="day__box"></span>Tue</span>
      <span class="day"><span class="day__box"></span>Wed</span>
      <span class="day"><span class="day__box"></span>Thurs</span>
      <span class="day"><span class="day__box"></span>Fri</span>
      <span class="day"><span class="day__box"></span>Sat</span>
    </div>
    <div class="field-row">
      <span class="field">NAME :<span class="field__line"></span></span>
      <span class="field">TIME :<span class="field__line"></span></span>
    </div>
    <div class="field-row">
      <span class="field">DATE :<span class="field__line"></span></span>
    </div>
  </div>
</section>

<section class="card card--contact">
  <div class="brand"><span class="brand__dot"></span>Keystone Physio</div>
  <div class="contact">
    <h1 class="contact__name">Mr Idris Malik</h1>
    <p class="contact__role">Osteopath(M.Ost)</p>
    <p class="contact__web">www.harlowkeystonephysio-example.com</p>

    <p class="contact__line">
      <svg class="icon" viewBox="0 0 24 24" aria-hidden="true"><path d="M6.6 10.8a15.1 15.1 0 0 0 6.6 6.6l2.2-2.2a1 1 0 0 1 1-.25 11.4 11.4 0 0 0 3.6.57 1 1 0 0 1 1 1V20a1 1 0 0 1-1 1A17 17 0 0 1 3 4a1 1 0 0 1 1-1h3.5a1 1 0 0 1 1 1c0 1.25.2 2.45.57 3.57a1 1 0 0 1-.25 1z"/></svg>
      07 3190 5627
    </p>
    <p class="contact__line">
      <svg class="icon" viewBox="0 0 24 24" aria-hidden="true"><path d="M2 5h20v14H2z"/><path d="M2 5l10 8 10-8" fill="none" stroke="#fff" stroke-width="2"/></svg>
      info@harlowkeystonephysio-example.com
    </p>

    <div class="location">
      <svg class="icon" viewBox="0 0 24 24" aria-hidden="true"><path d="M12 2a7 7 0 0 0-7 7c0 5.25 7 13 7 13s7-7.75 7-13a7 7 0 0 0-7-7zm0 9.5A2.5 2.5 0 1 1 12 6.5a2.5 2.5 0 0 1 0 5z"/></svg>
      <div>
        <span class="location__name">Keystone Physio Ridgeview</span><br>
        284 Mabel Street, Ridgeview QLD 4005
      </div>
    </div>
    <div class="location">
      <svg class="icon" viewBox="0 0 24 24" aria-hidden="true"><path d="M12 2a7 7 0 0 0-7 7c0 5.25 7 13 7 13s7-7.75 7-13a7 7 0 0 0-7-7zm0 9.5A2.5 2.5 0 1 1 12 6.5a2.5 2.5 0 0 1 0 5z"/></svg>
      <div>
        Keystone Physio Millyard Within Tallis Court<br>
        Lobby 1, Level 2, Millyard Square<br>
        58 Quillan Parade, Ashbrook QLD 4006
      </div>
    </div>
    <div class="location">
      <svg class="icon" viewBox="0 0 24 24" aria-hidden="true"><path d="M12 2a7 7 0 0 0-7 7c0 5.25 7 13 7 13s7-7.75 7-13a7 7 0 0 0-7-7zm0 9.5A2.5 2.5 0 1 1 12 6.5a2.5 2.5 0 0 1 0 5z"/></svg>
      <div>
        Keystone Physio Westmere Within Brightwell Medical Centre<br>
        Suite 6a, Level 1<br>
        812 Pemberton Road, Westmere QLD 4011
      </div>
    </div>
  </div>
</section>

</body>
</html>
```